Redesign this Sydney Chocolatier Website

We are looking for a redesign of this websites home page and product pages.

https://marlowconfections.com.au/

Marlow Confections have been making handmade chocolates in Sydney Australia since 1932 they specialize in making hand made chocolates without additives, without palm oil and using all-natural ingredients.

We are looking to rebrand the company to reposition the brand in the high-quality chocolate gifts and hampers market as such they have launched products to tackle this market.

https://marlowconfections.com.au/hampers-2/

Some of the players in this market that we would like to compete with are

https://www.thegiftcrategallery.com.au/

https://www.brindlecocoa.com.au/

https://www.chocolate.vesperine.com/

The website is currently built on Kavo Woo-commerce and though it looks decent in our opinion the home page is a little busy and does not convey the quality of the brand.

We are looking for something cleaner that will perform great especially on mobiles.

Target Market(s)

Families and business owners 40+ affluent we specialise in luxury chocolates hampers and chocolate gifts the current look lacks the high end look.

Number of Pages Required

2 page

Font styles to use
Script

Requirements
Must have
• Good SEO Footer, easy to navigate, cleaner than the original design, presents well on mobile devices, plant of room for copy I have included a copy doc with the actual home page copy.
Nice to have
• Something more stylish and high end looking that will appeal to the target market. clean navigation and easy to use that again translates well to mobile, you can use divs and read mores to declutter the long SEO texts see suggested copy doc (you do not have to use all of this
Should not have
• Less cluttered more stylish design than the original website

```html
<!DOCTYPE html>
<html lang="en">
<head>
<meta charset="utf-8">
<title>Marlow Confections — Homepage mobile version</title>
<link rel="stylesheet" href="https://fonts.googleapis.com/css2?family=Great+Vibes&family=Lora:ital,wght@0,400;0,600;0,700;1,400&family=Montserrat:wght@400;600&display=swap">
<style>
:root{
  --gold:#c2a574;
  --gold-dark:#a8895a;
  --cocoa:#1e0e07;
  --cocoa-2:#2b160b;
  --cream:#f6efe6;
  --paper:#faf8f5;
  --ink:#2a2a2a;
  --muted:#8b8b8b;
  --white:#ffffff;
}
*{margin:0;padding:0;box-sizing:border-box}
html,body{width:1200px;height:2193px;overflow:hidden;background:var(--white)}
body{position:relative;font-family:'Lora',serif;color:var(--ink)}
.page-title{position:absolute;left:0;right:0;top:140px;text-align:center;font-family:'Great Vibes',cursive;font-weight:400;font-size:104px;color:var(--cocoa-2);line-height:1}
.screen{position:absolute;width:238px;height:514px;border-radius:26px;overflow:hidden;background:var(--white);box-shadow:0 0 0 1px #e4e0da}
.c1{left:168px}.c2{left:482px}.c3{left:795px}
.r1{top:344px}.r2{top:928px}.r3{top:1513px}
.abs{position:absolute}
.row{position:absolute;left:0;right:0;text-align:center}
.script{font-family:'Great Vibes',cursive;font-weight:400;line-height:1.15}
.gold{color:var(--gold)}
.body-s{font-size:7.4px;line-height:15.6px}
.heading-gold{font-family:'Lora',serif;font-weight:700;color:var(--gold);font-size:14.5px;line-height:1.2}
.divider{position:absolute;left:50%;width:84px;margin-left:-42px;height:1px;background:var(--gold)}
.divider::after{content:"";position:absolute;left:39px;top:-1.5px;width:4px;height:4px;border-radius:50%;background:var(--gold)}
.divider.short{width:18px;margin-left:-9px;background:var(--gold)}
.divider.short::after{display:none}
.btn{position:absolute;background:var(--gold);color:var(--white);font-family:'Lora',serif;font-weight:600;font-size:7.5px;letter-spacing:.3px;display:flex;align-items:center;justify-content:center;border-radius:2px}
.dots{position:absolute;left:0;right:0;display:flex;justify-content:center;align-items:center;gap:7px}
.dot{width:6px;height:6px;border-radius:50%;background:#ddd}
.dot.on{width:11px;height:11px;border:1.5px solid var(--cocoa);background:radial-gradient(var(--cocoa) 40%,#fff 45%)}
.link{color:var(--gold);text-decoration:underline;font-size:7px;font-weight:600}
.readmore{font-size:7.5px;color:var(--gold);letter-spacing:.4px}
.wordmark{font-family:'Lora',serif;font-weight:400;color:var(--gold);line-height:1.1}
.search-band{position:absolute;left:0;top:0;width:100%;height:55px;background:var(--cocoa-2)}
.search{position:absolute;left:14px;right:14px;top:27px;height:20px;border-radius:10px;background:#4a3222;color:#d9cbbb;font-size:6.5px;padding-left:10px;display:flex;align-items:center}
.search svg{position:absolute;right:9px;top:6px}
.header{position:absolute;left:0;top:55px;width:100%;height:43px;background:var(--white)}
.hero{position:absolute;left:0;top:98px;width:100%;height:231px;background:radial-gradient(ellipse at 45% 20%,#5a3a24 0%,#2a1a10 45%,#1a0f09 100%)}
.eyebrow{display:inline-block;background:var(--gold-dark);color:#fff;font-size:5.6px;font-weight:700;line-height:8px;padding:0 3px;letter-spacing:.1px}
.info-strip{position:absolute;left:0;top:329px;width:100%;height:77px;background:var(--cream)}
.info-line{position:absolute;left:14px;right:14px;text-align:right;font-size:6.4px;line-height:9px;color:#555}
.info-title{font-weight:600;letter-spacing:.6px;color:var(--ink);font-size:6.6px}
.rule{position:absolute;height:1px;background:#d4c9ba}
.gold-panel{position:absolute;left:0;width:100%;background:linear-gradient(135deg,#c7ab7c,#b89a69 50%,#c4a878)}
.play{position:absolute;width:40px;height:40px;border-radius:50%;background:var(--cocoa-2);border:2px solid #8a6a40;display:flex;align-items:center;justify-content:center}
.dark{background:var(--cocoa)}
.foot-text{color:#e9e1d8;font-size:7.8px;line-height:16.2px}
.foot-h{color:#fff;font-size:12.5px;font-weight:600;line-height:1.2}
.foot-link{color:#e9e1d8;font-size:7.8px;line-height:1.3}
.social{display:inline-block;width:7px;height:7px;border-radius:50%;background:var(--gold);margin-left:6px;vertical-align:middle}
.tabbar{position:absolute;left:0;bottom:0;width:100%;height:43px;background:#fff;display:flex;justify-content:space-around;align-items:center}
.tab{display:flex;flex-direction:column;align-items:center;gap:2px;font-size:5.8px;color:#555}
</style>
</head>
<body>

<h1 class="page-title">Homepage - mobile version</h1>

<!-- Screen 1: header and hero -->
<section class="screen c1 r1">
  <div class="search-band">
    <div class="search">Search for gifts, &amp; hampers
      <svg width="7" height="7" viewBox="0 0 10 10"><circle cx="4" cy="4" r="3" fill="none" stroke="#bba" stroke-width="1.2"/><line x1="6.3" y1="6.3" x2="9" y2="9" stroke="#bba" stroke-width="1.2"/></svg>
    </div>
  </div>
  <header class="header">
    <div class="abs wordmark" style="left:14px;top:8px;font-size:16px">Marlow</div>
    <div class="abs" style="left:14px;top:29px;font-size:3.6px;line-height:5px;color:var(--gold);letter-spacing:.3px">YOUR CHOCOLATIER SINCE 1932</div>
    <svg class="abs" style="left:206px;top:14px" width="16" height="16" viewBox="0 0 16 16"><rect width="16" height="16" rx="4" fill="#f1f1f1"/><path d="M5 5.5h6M5 8h6M5 10.5h6" stroke="#222" stroke-width="1"/></svg>
  </header>
  <div class="hero" role="img" aria-label="Melted chocolate poured from a spoon into a wooden bowl">
    <div class="row" style="top:53px;line-height:8px"><span class="eyebrow">HANDCRAFTED CHOCOLATES MADE IN SYDNEY SINCE 1932</span></div>
    <div class="row script" style="top:66px;color:#fff;font-size:17px;line-height:20px">Welcome To Marlow Confections</div>
    <div class="row" style="top:94px;color:#fff;font-size:7.5px;line-height:15.6px">Chillwave glossier bespoke next level, pinterest<br>literally truffaut meditation squid food trucksetola.</div>
    <div class="btn" style="left:70px;top:144px;width:98px;height:36px;font-size:7.5px">SHOP NOW</div>
    <div class="dots" style="top:205px"><span class="dot"></span><span class="dot on" style="border-color:#fff;background:radial-gradient(#fff 40%,transparent 45%)"></span><span class="dot"></span></div>
  </div>
  <div class="info-strip">
    <div class="rule" style="left:14px;right:58px;top:18px"></div>
    <div class="info-line info-title" style="top:14px">FREE SHIPPING</div>
    <div class="info-line" style="top:25px">Lorem Ipsumat Dolor Text Filler For The Design Purposes Only</div>
    <div class="rule" style="left:14px;right:58px;top:48px"></div>
    <div class="info-line info-title" style="top:44px">LOREMAT IPSUM</div>
    <div class="info-line" style="top:56px">Lorem Ipsumat Dolor Text Filler For The Design Purposes Only</div>
  </div>
  <div class="row script gold" style="top:452px;font-size:25px;line-height:27px">- Welcome to Marlow -<br>your chocolatier since 1932</div>
</section>

<!-- Screen 2: story -->
<section class="screen c2 r1">
  <div class="abs" style="left:0;top:0;width:100%;height:55px;background:var(--cream)">
    <div class="info-line" style="top:4px;text-align:center;font-size:6px">Lorem Ipsumat Dolor Text Filler For The Design Purposes Only</div>
    <div class="rule" style="left:14px;right:78px;top:26px"></div>
    <div class="info-line info-title" style="top:22px">LOREMAT IPSUM</div>
    <div class="info-line" style="top:33px">Lorem Ipsumat Dolor Text Filler For The Design Purposes Only</div>
  </div>
  <div class="abs script gold" style="left:12px;right:0;top:100px;font-size:25px;line-height:27px;text-align:center">- Welcome to Marlow -<br>your chocolatier since 1932</div>
  <p class="abs body-s" style="left:14px;right:14px;top:174px;font-size:7.6px">Marlow Confections was founded by Arthur Marlow in 1932. Arthur always had a passion for making handmade chocolate from his kitchen in Paddington. In time, he became a master at his craft and developed a loyal customer for following. From his efforts, some of Australia's most delicious fondants, hard centres, jellies and gingers coated with the finest chocolate were conceived.</p>
  <div class="abs readmore" style="left:14px;top:316px">READ MORE &#8594;</div>
  <div class="rule" style="left:14px;right:14px;top:337px"></div>
  <div class="abs" style="left:18px;top:349px;font-size:6.5px;line-height:9px;color:var(--muted);letter-spacing:.6px">NEED A CHOCOLATE FOR SPECIAL OCCASIONS?</div>
  <div class="abs" style="left:18px;top:360px;font-size:8.2px;line-height:11px;font-weight:600;color:var(--ink)">Give us a call, or place your order online!</div>
  <div class="btn" style="left:18px;top:387px;width:101px;height:37px">PLACE ORDER</div>
  <div class="abs" style="left:0;top:476px;width:100%;height:38px;background:#f3f3f3"></div>
</section>

<!-- Screen 3: products -->
<section class="screen c3 r1" style="background:var(--paper)">
  <div class="row heading-gold" style="top:22px">Our Handmade Chocolate</div>
  <div class="divider" style="top:51px"></div>
  <div class="row" style="top:62px;font-size:6.8px;line-height:15.6px;color:var(--muted)">Lorem Ipsum is simply dummy text of the printing and the<br>typesetting industry.</div>
  <div class="row" style="top:110px;font-size:6.2px;line-height:9px;color:#777"><span style="color:var(--ink)">DARK CHOCOLATE</span> &nbsp;/&nbsp; MILK CHOCOLATES &nbsp;/&nbsp; SOFT CENTRES</div>
  <div class="abs" style="left:19px;top:138px;width:209px;height:219px;background:#f3f3f3" role="img" aria-label="Gift box of chocolate-coated ginger with an orange handle"></div>
  <svg class="abs" style="left:203px;top:138px" width="25" height="25" viewBox="0 0 25 25"><path d="M0 0H25V25Z" fill="var(--cocoa)"/><path d="M15 6h6M18 3v6" stroke="#fff" stroke-width="1"/></svg>
  <div class="abs" style="left:19px;top:366px;font-size:8.5px;line-height:11px;color:#444">Take Me Along</div>
  <div class="abs" style="right:10px;top:366px;font-size:8.5px;line-height:11px;font-weight:600;color:var(--ink)">$29.76</div>
  <div class="abs" style="left:19px;top:379px;font-size:5.8px;line-height:8px;color:var(--muted)">Net. Weight: 150gr</div>
  <div class="btn" style="left:19px;top:402px;width:209px;height:32px">ADD TO CART</div>
  <div class="dots" style="top:452px"><span class="dot"></span><span class="dot on"></span><span class="dot"></span></div>
  <div class="row" style="top:479px;font-size:7px;line-height:10px;color:var(--ink)">Didn't find what you are looking for?</div>
  <div class="row" style="top:491px;line-height:10px"><span class="link">Click here to view all selections &amp; products</span></div>
</section>

<!-- Screen 4: brand story panel -->
<section class="screen c1 r2" style="background:var(--paper)">
  <div class="row" style="top:21px;line-height:10px"><span class="link">Click here to view all selections &amp; products</span></div>
  <div class="gold-panel" style="top:83px;height:346px" role="img" aria-label="Gold background with embossed chocolate pattern">
    <div class="row script" style="top:50px;font-size:23px;line-height:27px;color:var(--cocoa)">Marlow Confections –<br>Handmade Chocolate</div>
    <div class="divider" style="top:117px;background:var(--cocoa)"></div>
    <div class="row" style="top:128px;font-size:7.8px;line-height:15.6px;color:#fff">Holidays, birthdays, anniversaries... No matter what<br>you're celebrating, you'll find in our handmade<br>chocolates the perfect gift for any occasion.</div>
    <div class="abs" style="left:54px;top:206px;font-size:9px;line-height:12px;color:var(--cocoa)">WATCH</div>
    <div class="play" style="left:99px;top:192px"><svg width="12" height="12" viewBox="0 0 12 12"><path d="M2 0L12 6 2 12Z" fill="#fff"/></svg></div>
    <div class="abs" style="left:149px;top:206px;font-size:9px;line-height:12px;color:var(--cocoa)">VIDEO</div>
    <div class="row" style="top:246px;font-size:7.8px;line-height:15.6px;color:#fff">Hand-crafted and hand-wrapped, make someone<br>feel special with their favourite Marlow chocolate<br>flavour; made with love in Sydney since 1932.</div>
  </div>
  <div class="row heading-gold" style="top:478px">Discover Chocolates</div>
  <div class="divider" style="top:505px;width:90px;margin-left:-45px"></div>
</section>

<!-- Screen 5: gifts and hampers -->
<section class="screen c2 r2">
  <div class="row heading-gold" style="top:26px">Discover Chocolates</div>
  <div class="divider" style="top:55px"></div>
  <div class="row" style="top:66px;font-size:6.8px;line-height:15.6px;color:var(--muted)">Lorem Ipsum is simply dummy text of the printing and the<br>typesetting industry.</div>
  <div class="abs" style="left:48px;top:126px;width:141px;height:8px;background:var(--gold)"></div>
  <div class="abs" style="left:20px;top:133px;width:198px;height:309px;background:var(--paper);border:1px solid #e6e2dc"></div>
  <div class="abs" style="left:48px;top:160px;width:142px;height:86px;background:radial-gradient(ellipse,#c9584d 0%,#b9a37a 50%,#faf8f5 75%)" role="img" aria-label="Chocolate hamper with gift boxes and treats"></div>
  <div class="abs" style="left:14px;top:276px;width:210px;height:41px;background:var(--cocoa);display:flex;align-items:center;justify-content:center">
    <span class="script" style="color:#fff;font-size:22px">Gifts &amp; Hampers</span>
  </div>
  <div class="row" style="top:339px;font-size:7.5px;line-height:15.6px;color:var(--ink)">Check out our ever-expanding<br>collection of chocolate hampers and<br>keep an eye out for our holiday<br>specials. To get the best of Marlow...<br>Make it a hamper!</div>
  <div class="btn" style="left:48px;top:443px;width:141px;height:21px;font-size:6.6px">CLICK TO VIEW PRODUCTS</div>
  <div class="dots" style="top:487px"><span class="dot"></span><span class="dot on"></span><span class="dot"></span></div>
</section>

<!-- Screen 6: testimonials -->
<section class="screen c3 r2">
  <div class="abs" style="left:0;top:30px;width:100%;height:467px;background:radial-gradient(ellipse at 50% 60%,#2e1c12 0%,#160b06 70%)" role="img" aria-label="Dark chocolate photo background with cocoa and spoon">
    <div class="row script gold" style="top:45px;font-size:27px;line-height:30px">Our Testimonials</div>
    <div class="divider" style="top:83px"></div>
    <div class="row" style="top:95px;font-size:7.5px;line-height:16px;color:#fff">Lorem Ipsum is simply dummy text of the printing and the<br>typesetting industry.</div>
    <div class="abs" style="left:9px;top:158px;width:218px;height:151px;border:1px solid var(--gold)"></div>
    <svg class="abs" style="left:110px;top:185px" width="14" height="12" viewBox="0 0 14 12"><path d="M0 6Q0 0 6 0V2Q3 2 3 5H6V12H0ZM8 6Q8 0 14 0V2Q11 2 11 5H14V12H8Z" fill="var(--gold)"/></svg>
    <div class="row" style="top:213px;font-size:7.6px;line-height:16.3px;color:#fff">Marlow chocolates are absolutely delicious.<br>We order often and now have family<br>ordering too. Great quality and the cream are<br>my absolute favorite!</div>
    <svg class="abs" style="left:112px;top:308px" width="10" height="6" viewBox="0 0 10 6"><path d="M0 0L5 5 10 0" fill="#1a0e08" stroke="var(--gold)"/></svg>
    <div class="abs" style="left:102px;top:328px;width:32px;height:32px;border-radius:50%;background:#e9ddd0;border:2px solid #fff" role="img" aria-label="Customer portrait"></div>
    <div class="row" style="top:366px;font-size:8.5px;line-height:11px;font-weight:600;color:#fff">Clara Wendell</div>
    <div class="row" style="top:380px;font-size:6.4px;line-height:9px;color:#cbbfb2">- Satisfied Costumer</div>
    <svg class="abs" style="left:82px;top:401px" width="14" height="10" viewBox="0 0 14 10"><path d="M13 5H1M5 1L1 5 5 9" fill="none" stroke="#fff"/></svg>
    <svg class="abs" style="left:142px;top:401px" width="14" height="10" viewBox="0 0 14 10"><path d="M1 5H13M9 1L13 5 9 9" fill="none" stroke="#fff"/></svg>
  </div>
</section>

<!-- Screen 7: palm oil free -->
<section class="screen c1 r3">
  <div class="abs" style="left:11px;top:60px;width:217px;height:221px;border-top:1px solid var(--gold);border-right:1px solid var(--gold)"></div>
  <div class="abs" style="left:11px;top:66px;width:211px;height:215px;background:radial-gradient(ellipse at 55% 40%,#3a2418 0%,#6b4a38 35%,#f2f2f2 70%)" role="img" aria-label="Broken pieces of dark chocolate"></div>
  <div class="abs script gold" style="left:11px;top:306px;font-size:22px;line-height:26px;white-space:nowrap">Handmade-Palm Oil Free</div>
  <p class="abs" style="left:11px;right:10px;top:341px;font-size:7.6px;line-height:16.2px;color:var(--ink)">All of our chocolate is real chocolate! A few years ago, Marlow (like many chocolatiers) was using compound chocolate which contains palm oil. The compound chocolate is popular with chocolate makers as it has a higher melting point and is easier to work with...</p>
  <div class="abs readmore" style="left:11px;top:437px">READ MORE &#8594;</div>
  <div class="abs" style="left:0;top:502px;width:100%;height:12px;background:var(--cream)"></div>
</section>

<!-- Screen 8: subscribe and footer -->
<section class="screen c2 r3 dark">
  <div class="abs" style="left:0;top:0;width:100%;height:164px;background:var(--cream)">
    <div class="row script gold" style="top:30px;font-size:30px;line-height:34px">Subscribe Here</div>
    <div class="abs" style="left:9px;top:77px;width:122px;height:32px;background:#fff;border:1px solid #e4dcd0;font-size:6.6px;color:#999;display:flex;align-items:center;padding-left:8px">Enter Your E-mail Address</div>
    <div class="btn" style="left:131px;top:77px;width:95px;height:32px;font-size:7.5px;border-radius:0">SUBSCRIBE NOW</div>
  </div>
  <div class="row wordmark" style="top:210px;font-size:22px">Marlow</div>
  <div class="row" style="top:238px;font-size:4.6px;line-height:6px;color:var(--gold);letter-spacing:.3px">YOUR CHOCOLATIER<br>SINCE 1932</div>
  <div class="row foot-text" style="top:268px">We handcraft unique, mouth-watering<br>milk and dark chocolate creations for<br>chocolate aficionados in Sydney and<br>throughout Australia.</div>
  <div class="row foot-h" style="top:358px">Quick Links</div>
  <div class="divider short" style="top:382px"></div>
  <div class="row foot-link" style="top:397px">» Recipes</div>
  <div class="row foot-link" style="top:417px">» Terms and Conditions</div>
  <div class="row foot-link" style="top:436px">» Privacy Policy</div>
  <div class="row foot-link" style="top:454px">» Shopping Policy</div>
  <div class="row foot-link" style="top:473px">» Sitemap</div>
</section>

<!-- Screen 9: footer contact -->
<section class="screen c3 r3 dark">
  <div class="row foot-text" style="top:23px">We handcraft unique, mouth-watering<br>milk and dark chocolate creations for<br>chocolate aficionados in Sydney and<br>throughout Australia.</div>
  <div class="row foot-h" style="top:113px">Quick Links</div>
  <div class="divider short" style="top:137px"></div>
  <div class="row foot-link" style="top:153px">» Recipes</div>
  <div class="row foot-link" style="top:173px">» Terms and Conditions</div>
  <div class="row foot-link" style="top:191px">» Privacy Policy</div>
  <div class="row foot-link" style="top:210px">» Shopping Policy</div>
  <div class="row foot-link" style="top:228px">» Sitemap</div>
  <div class="row foot-h" style="top:267px">Contact Information</div>
  <div class="divider short" style="top:292px"></div>
  <div class="row foot-link" style="top:308px"><b>Location:</b> 42 Harbourview Rd - Lindfield</div>
  <div class="row foot-link" style="top:327px">NSW, Australia</div>
  <div class="row foot-link" style="top:346px"><b>Phone Number:</b> +61 2 9000 4417</div>
  <div class="row foot-link" style="top:365px"><b>Email:</b> hello@marlowconfections.com.au</div>
  <div class="row foot-link" style="top:382px"><b>Find Us At:</b><span class="social"></span><span class="social"></span><span class="social"></span><span class="social"></span><span class="social"></span></div>
  <div class="abs" style="left:0;top:433px;width:100%;height:34px;background:#0c0604;display:flex;align-items:center;justify-content:center;font-size:6.8px;color:#fff"><span class="gold">Marlow Confections 2020</span>&nbsp;© All Rights Reserved</div>
  <nav class="tabbar">
    <div class="tab"><svg width="10" height="10" viewBox="0 0 10 10"><path d="M0 0h4v4H0zM6 0h4v4H6zM0 6h4v4H0zM6 6h4v4H6z" fill="var(--gold)"/></svg>Shop</div>
    <div class="tab"><svg width="10" height="10" viewBox="0 0 10 10"><path d="M5 9L1 5A2.4 2.4 0 0 1 5 2 2.4 2.4 0 0 1 9 5Z" fill="var(--gold)"/></svg>Wishlist</div>
    <div class="tab"><svg width="10" height="10" viewBox="0 0 10 10"><path d="M1 3h8v7H1zM3 3V1.5h4V3" fill="var(--gold)"/></svg>Cart</div>
    <div class="tab"><svg width="10" height="10" viewBox="0 0 10 10"><circle cx="5" cy="3" r="2.4" fill="var(--gold)"/><path d="M0.5 10a4.5 4 0 0 1 9 0Z" fill="var(--gold)"/></svg>My Account</div>
  </nav>
</section>

</body>
</html>
```